Loan broker seeks referral card design for real estate financing

We need a design for a referral card for people who recommend us for real estate financing. If the deal goes through, each referrer will receive €750.

Text similar to: Recommend me! For every successful real estate financing referral, you will receive €750. (Other suggestions are also welcome)

The size should be no larger than A5 format, or possibly even oblong.
The design should convey security and competence and include themes such as independent advice.

The design should also include the company logo and a photo of me. Naturally, the design should also include a link to my website: www.die-brennholt.at, along with my phone number and email address: office@die-brennholt.at

```html
<!DOCTYPE html>
<html lang="de">
<head>
<meta charset="utf-8">
<title>Empfehlungskarte – Brennholt Finanz GmbH</title>
<link href="https://fonts.googleapis.com/css2?family=Lexend:wght@400;500;600&display=swap" rel="stylesheet">
<style>
  :root {
    --page-bg: #e6e6e6;
    --card-bg: #f8f8f8;
    --brand-blue: #2b58a6;
    --text-grey: #5e5e5e;
    --rule-grey: #6a6a6a;
    --white: #ffffff;
    --photo-light: #cfcbcd;
    --photo-dark: #34323b;
  }
  * { margin: 0; padding: 0; box-sizing: border-box; }
  html, body {
    width: 1200px; height: 1124px; overflow: hidden;
    background: var(--page-bg);
    font-family: "Lexend", sans-serif;
  }
  .referral-card {
    position: absolute; left: 40px; top: 167px;
    width: 1120px; height: 789px;
    background: var(--card-bg);
    overflow: hidden;
  }
  .brand {
    position: absolute; left: 57px; top: 53px;
    display: flex; align-items: center; gap: 22px;
  }
  .brand-mark {
    width: 143px; height: 143px; border-radius: 50%;
    border: 5px solid var(--brand-blue);
  }
  .brand-divider {
    width: 4px; height: 145px; background: var(--rule-grey);
  }
  .brand-text { display: flex; flex-direction: column; gap: 6px; }
  .brand-name {
    color: var(--brand-blue); font-weight: 500; font-size: 27px; line-height: 1.1;
  }
  .brand-tagline {
    color: var(--text-grey); font-weight: 400; font-size: 19px; line-height: 1.1;
  }
  .advisor-photo {
    position: absolute; left: 748px; top: 56px;
    width: 372px; height: 628px;
    background: linear-gradient(160deg, var(--photo-light) 0%, var(--photo-dark) 100%);
  }
  .headline {
    position: absolute; left: 56px; top: 258px;
    color: var(--brand-blue); font-weight: 600; font-size: 47px; line-height: 1;
  }
  .offer {
    position: absolute; left: 56px; top: 344px;
    color: var(--text-grey); font-weight: 600; font-size: 50px; line-height: 67px;
  }
  .bonus {
    position: absolute; left: 54px; top: 548px;
    color: var(--brand-blue); font-weight: 600; font-size: 86px; line-height: 1;
  }
  .contact-band {
    position: absolute; left: 0; bottom: 0;
    width: 100%; height: 105px;
    background: var(--brand-blue);
    border-top: 3px solid var(--rule-grey);
    display: flex; align-items: center; gap: 20px;
    padding-left: 49px;
  }
  .contact-item {
    display: flex; align-items: center; gap: 9px;
    color: var(--white); font-weight: 500; font-size: 30px; white-space: nowrap;
  }
  .contact-icon { width: 35px; height: 35px; flex: none; }
</style>
</head>
<body>
  <div class="referral-card">
    <div class="brand">
      <div class="brand-mark"></div>
      <div class="brand-divider"></div>
      <div class="brand-text">
        <span class="brand-name">Brennholt Finanz GmbH</span>
        <span class="brand-tagline">Finanzieren, Versichern, Vorsorgen</span>
      </div>
    </div>

    <div class="advisor-photo" role="img" aria-label="Porträtfoto des Beraters im dunklen Sakko und weißen Hemd"></div>

    <h1 class="headline">Empfehlen Sie mich weiter!</h1>
    <p class="offer">Für jede realisierte<br>Immobilienfinanzierung<br>erhalten Sie als Tippgeber</p>
    <p class="bonus">€ 750</p>

    <div class="contact-band">
      <span class="contact-item">
        <svg class="contact-icon" viewBox="0 0 36 36" aria-hidden="true">
          <circle cx="18" cy="18" r="18" fill="#fff"/>
          <path d="M12 10c1-1 2-1 3 0l2 3c.5 1 .3 1.8-.5 2.4l-1 .8c.9 2 2.4 3.6 4.4 4.5l.8-1c.6-.8 1.4-1 2.4-.5l3 2c1 .7 1 1.8 0 2.8l-1.4 1.3c-1.5 1.3-4 .8-7-1.4-3-2.3-5.4-5.4-6.3-8.2-.6-2-.4-3.5.6-4.6z" fill="#2b58a6"/>
        </svg>
        (123) 555 017
      </span>
      <span class="contact-item">
        <svg class="contact-icon" viewBox="0 0 36 36" aria-hidden="true">
          <circle cx="18" cy="18" r="18" fill="#fff"/>
          <rect x="10" y="12" width="16" height="12" rx="1" fill="none" stroke="#2b58a6" stroke-width="1.6"/>
          <path d="M10 12l8 7 8-7M10 24l6-6M26 24l-6-6" fill="none" stroke="#2b58a6" stroke-width="1.4"/>
        </svg>
        office@die-brennholt.at
      </span>
      <span class="contact-item">
        <svg class="contact-icon" viewBox="0 0 36 36" aria-hidden="true">
          <circle cx="18" cy="18" r="18" fill="#fff"/>
          <g fill="none" stroke="#2b58a6" stroke-width="1.4">
            <circle cx="18" cy="18" r="8"/>
            <ellipse cx="18" cy="18" rx="3.5" ry="8"/>
            <path d="M10 18h16M11.2 14h13.6M11.2 22h13.6M18 10v16"/>
          </g>
        </svg>
        www.die-brennholt.at
      </span>
    </div>
  </div>
</body>
</html>
```